Organic skincare label - minimalist, earthy, luxe design needed!

I need a label design for a luxury natural skin care line called "Velka Botanix". Velka means 'earth' in Swahili. I would like the design to embody an earthy feel but be minimalistic and give a luxe vibe. My first product will be a Tumeric and Neem Scrub.

The size of the jar is 8oz, label dimensions should be (1.625" Tall x 8.5" Wide)
I will be making other products too such as; oils + toners so I feel free to do labels for glass bottles and/or spray bottles as well.

Forest green, light pinks/nudes/beige, grey, white, gold, are colors that can be used (not all have to be used).

I have included pictures of some things I've worked on myself as well as my original logo design but I need to simplify the logo, no circle around it.
Feel free to get creative.

Thank you! :)
Updates

Target Market(s)

Socially Conscious, Beauty Enthusiast, Minimalist

Industry/Entity Type

Skin Care

Font styles to use
Sans Serif
Other font styles liked:
• "Wonderlove doodle" is the font used for "Velka" in the logo. Feel free to use that or change it as you see fit.

Requirements
Must have
• Simplistic design
would like to stick to a font close to the ones in the logo. Either the one used for the name "Velka" OR the one that the slogan "Grounded Tonics" uses.

I have also included some pictures to capture the aesthetic of my social media and website.

Gender neutral

```html
<!DOCTYPE html>
<html lang="en">
<head>
<meta charset="utf-8">
<title>Velka Botanix — Tumeric and Neem Scrub Labels</title>
<link href="https://fonts.googleapis.com/css2?family=Poppins:wght@400;500;600&display=swap" rel="stylesheet">
<style>
  :root {
    --backdrop: #dddcdd;
    --forest: #2c3128;
    --forest-deep: #262b23;
    --copper: #c28b6d;
    --copper-light: #d4a283;
    --white: #f6f4f1;
    --gold-1: #b8862e;
    --gold-2: #e2c26a;
    --gold-3: #8f6a2a;
  }
  * { box-sizing: border-box; margin: 0; padding: 0; }
  html, body { width: 1200px; height: 1200px; overflow: hidden; }
  body {
    background: var(--backdrop);
    font-family: "Poppins", sans-serif;
    position: relative;
  }

  /* Round lid label */
  .lid-label {
    position: absolute;
    left: 68px; top: 484px;
    width: 480px; height: 480px;
    border-radius: 50%;
    background: linear-gradient(135deg, var(--gold-2) 0%, var(--gold-1) 45%, var(--gold-3) 100%);
    display: flex; align-items: center; justify-content: center;
  }
  .lid-label__face {
    width: 344px; height: 344px;
    border-radius: 50%;
    background: var(--forest);
    display: flex; flex-direction: column; align-items: center; justify-content: center;
    text-align: center;
    padding-top: 20px;
  }

  /* Jar band label */
  .jar-label {
    position: absolute;
    left: 588px; top: 322px;
    width: 448px; height: 228px;
    background: var(--forest);
    display: flex; flex-direction: column; align-items: center; justify-content: center;
    text-align: center;
    padding-top: 14px;
  }

  /* Box front panel */
  .box-panel {
    position: absolute;
    left: 554px; top: 550px;
    width: 512px; height: 406px;
    background: var(--forest-deep);
    padding: 0 42px 26px 0;
    display: flex; flex-direction: column; justify-content: flex-end; align-items: flex-end;
    text-align: right;
  }

  /* Shared brand lockup */
  .brand-name {
    color: var(--copper);
    font-weight: 600;
    letter-spacing: 0.02em;
    line-height: 1;
  }
  .brand-tagline {
    color: var(--copper);
    font-weight: 500;
    text-transform: uppercase;
    letter-spacing: 0.12em;
  }
  .product-name { color: var(--white); font-weight: 400; }
  .product-size { color: var(--white); font-weight: 400; opacity: 0.85; }

  .lid-label .brand-name { font-size: 40px; }
  .lid-label .brand-tagline { font-size: 9px; margin-top: 6px; }
  .lid-label .product-name { font-size: 17px; margin-top: 20px; }
  .lid-label .product-size { font-size: 6.5px; margin-top: 14px; }

  .jar-label .brand-name { font-size: 48px; }
  .jar-label .brand-tagline { font-size: 11px; margin-top: 8px; }
  .jar-label .product-name { font-size: 22px; margin-top: 24px; }
  .jar-label .product-size { font-size: 9px; margin-top: 20px; }

  .ingredients {
    color: var(--copper-light);
    font-size: 16px;
    line-height: 29px;
    font-weight: 400;
  }
  .origin {
    color: var(--copper);
    font-size: 15.5px;
    font-weight: 600;
    margin-top: 14px;
  }
</style>
</head>
<body>

  <div class="lid-label">
    <div class="lid-label__face">
      <div class="brand-name">Velka</div>
      <div class="brand-tagline">Grounded Tonics</div>
      <div class="product-name">Tumeric and Neem Scrub</div>
      <div class="product-size">8oz / 59ml</div>
    </div>
  </div>

  <div class="jar-label">
    <div class="brand-name">Velka</div>
    <div class="brand-tagline">Grounded Tonics</div>
    <div class="product-name">Tumeric and Neem Scrub</div>
    <div class="product-size">8oz / 59ml</div>
  </div>

  <div class="box-panel">
    <p class="ingredients">
      Ingredients Organic Rosehip<br>
      Seed Oil, Organic Camelia Seed<br>
      Oil, Organic Pomegranate<br>
      Oil, VitaminE non-GMO
    </p>
    <p class="origin">MADE IN MARLOW, TX</p>
  </div>

</body>
</html>
```